Simple elegant feminine design - Going out on my own as a Mortgage Broker.
My thoughts are the following details on the Front, middle of the card possibly? Phone and email smaller font than my name?
Marnie Veltrin
Finance Specialist
p: 0438 215 962
e: marnie@veltrinlending.com.au
Bottom of the card
residential / commercial / equipment
I would like the Font in Rose Gold maybe white or black background? or Possibly a stone grey - are you able to do a few options? I'd like them embossed
Then I had an idea as a simple logo as per the attached if you get the idea in my scribble, my initials, capital M attached to a small v that leads/follows into a circle? Thicker Font In Rose Gold, middle of the card at the back.
Very open to ideas though and what colour you think would look better with the Rose Gold.
Thanks so much for your help, I am not very creative and savvy with this stuff :-)
Industry/Entity Type
Finance
Contact Information for Business Card
Marnie Veltrin
p: 0438 215 962
Look and feel

```html
<!DOCTYPE html>
<html lang="en">
<head>
<meta charset="utf-8">
<title>Marnie Veltrin – Finance Specialist</title>
<link rel="stylesheet" href="https://fonts.googleapis.com/css2?family=Raleway:wght@400;500&display=swap">
<style>
  :root {
    --paper: #ffffff;
    --ink: #0d0d0d;
    --gold-light: #f8e39a;
    --gold-mid: #e0b458;
    --gold-deep: #b07a22;
    --envelope-line: #e8c46e;
  }
  html, body {
    margin: 0;
    padding: 0;
    width: 1200px;
    height: 720px;
    overflow: hidden;
    background: var(--paper);
  }
  .card {
    position: relative;
    width: 1200px;
    height: 720px;
    background: var(--paper);
    color: var(--ink);
    font-family: "Raleway", sans-serif;
  }
  .identity {
    position: absolute;
    top: 138px;
    left: 0;
    width: 100%;
    text-align: center;
  }
  .identity__name {
    margin: 0;
    font-family: "Raleway", sans-serif;
    font-weight: 500;
    font-size: 74px;
    line-height: 1;
    letter-spacing: 1px;
    color: var(--ink);
  }
  .identity__role {
    margin: 18px 0 0;
    font-size: 35px;
    font-weight: 400;
    line-height: 1.1;
    letter-spacing: 0.5px;
  }
  .contact {
    position: absolute;
    left: 0;
    width: 100%;
    text-align: center;
  }
  .contact--phone { top: 402px; }
  .contact--email { top: 531px; }
  .contact__icon {
    display: block;
    width: 52px;
    height: 52px;
    margin: 0 auto 6px;
  }
  .contact__text {
    display: block;
    font-size: 38px;
    font-weight: 400;
    line-height: 1.1;
    letter-spacing: 0.5px;
  }
</style>
</head>
<body>
  <svg width="0" height="0" style="position:absolute" aria-hidden="true">
    <defs>
      <linearGradient id="gold-disc" x1="0" y1="0" x2="1" y2="1">
        <stop offset="0" stop-color="#f8e39a"/>
        <stop offset="0.5" stop-color="#e0b458"/>
        <stop offset="1" stop-color="#b07a22"/>
      </linearGradient>
    </defs>
  </svg>

  <main class="card">
    <header class="identity">
      <h1 class="identity__name">Marnie Veltrin</h1>
      <p class="identity__role">Finance Specialist</p>
    </header>

    <div class="contact contact--phone">
      <svg class="contact__icon" viewBox="0 0 52 52" aria-hidden="true">
        <circle cx="26" cy="26" r="26" fill="url(#gold-disc)"/>
        <path d="M19.5 15.5c1-.6 2.1-.3 2.7.6l2.2 3.4c.5.8.4 1.9-.4 2.5l-1.6 1.2c.9 2.3 2.7 4.4 5 5.8l1.4-1.4c.7-.7 1.8-.8 2.5-.2l3.2 2.4c.9.7 1.1 1.9.4 2.8l-1.5 2c-.8 1-2.2 1.4-3.5 1-6.6-2.3-11.4-7.5-13.1-14.1-.3-1.3.2-2.6 1.300-3.4z" fill="#111"/>
      </svg>
      <span class="contact__text">0438 215 962</span>
    </div>

    <div class="contact contact--email">
      <svg class="contact__icon" viewBox="0 0 52 52" aria-hidden="true">
        <circle cx="26" cy="26" r="26" fill="url(#gold-disc)"/>
        <rect x="14" y="18" width="24" height="16" rx="1.5" fill="#111"/>
        <path d="M14.8 19l11.2 8.6 11.2-8.6" fill="none" stroke="#e8c46e" stroke-width="1.4"/>
        <path d="M14.8 33l8.4-6.6M37.2 33l-8.4-6.6" fill="none" stroke="#e8c46e" stroke-width="1.2"/>
      </svg>
      <span class="contact__text">marnie@veltrinlending.com.au</span>
    </div>
  </main>
</body>
</html>
```